Flyer-Design für Shop für nachhaltige Haustierprodukte
Tolle Umsetzung nach den Vorgaben. Änderungen super und schnell umgesetzt. Gerne wieder!
Zielgruppe
MELBOR ist ein Online-Marktplatz für nachhaltige Haustierprodukte. Meine Zielgruppe sind Frauen zwischen 30 und 60 Jahren mit Haustieren (Hund, Katze, Pferd)
Aufgabenstellung
Das Design soll an der Webseite angepasst sein. Es ist wichtig, dass das Thema Nachhaltigkeit kommuniziert wird und welche Vorteile MELBOR hat (Markenvielvalt, kleine Manufakturen, Handmade etc.)

```html
<!DOCTYPE html>
<html lang="de">
<head>
<meta charset="utf-8">
<title>MELBOR – Flyer</title>
<link rel="stylesheet" href="https://fonts.googleapis.com/css2?family=Montserrat:wght@300;500;700&display=swap">
<style>
  :root {
    --orange: #ec7630;
    --white: #ffffff;
    --photo-dark: #4a3a30;
    --photo-mid: #8a7866;
    --photo-light: #b9ada0;
  }
  html, body {
    margin: 0;
    padding: 0;
    width: 1200px;
    height: 2400px;
    overflow: hidden;
    background: var(--white);
  }
  .flyer {
    position: relative;
    width: 1200px;
    height: 2400px;
    overflow: hidden;
    font-family: "Montserrat", sans-serif;
    background: var(--white);
  }
  .brand {
    position: absolute;
    left: 102px;
    top: 124px;
    width: 966px;
    height: 160px;
    display: flex;
    align-items: center;
    gap: 26px;
  }
  .brand-dot {
    width: 154px;
    height: 154px;
    border: 4px solid var(--orange);
    border-radius: 50%;
    box-sizing: border-box;
    flex: none;
  }
  .brand-name {
    font-weight: 500;
    font-size: 156px;
    line-height: 1;
    color: var(--orange);
    letter-spacing: 2px;
    white-space: nowrap;
  }
  .benefits {
    position: absolute;
    left: 0;
    top: 399px;
    width: 1200px;
    height: 1017px;
    background: var(--orange);
    color: var(--white);
  }
  .headline {
    position: absolute;
    left: 121px;
    top: 96px;
    margin: 0;
    font-weight: 700;
    font-size: 80px;
    line-height: 101px;
    letter-spacing: 0.5px;
  }
  .benefit-list {
    position: absolute;
    left: 121px;
    top: 426px;
    margin: 0;
    padding: 0;
    list-style: none;
  }
  .benefit-list li {
    display: flex;
    align-items: center;
    height: 81px;
    font-weight: 300;
    font-size: 43px;
    letter-spacing: 0.3px;
    white-space: nowrap;
  }
  .benefit-list svg {
    width: 52px;
    height: 52px;
    margin-right: 46px;
    flex: none;
  }
  .photo {
    position: absolute;
    left: 0;
    top: 1416px;
    width: 1200px;
    height: 772px;
    background: radial-gradient(ellipse at 55% 55%, var(--photo-mid) 0%, var(--photo-dark) 45%, var(--photo-light) 100%);
  }
  .website {
    position: absolute;
    left: 121px;
    top: 2255px;
    font-weight: 700;
    font-size: 57px;
    line-height: 1;
    color: var(--orange);
    letter-spacing: 0.3px;
  }
  .animal-marks {
    position: absolute;
    left: 743px;
    top: 2242px;
    display: flex;
    gap: 29px;
  }
  .animal-marks span {
    width: 94px;
    height: 94px;
    border: 4px solid var(--orange);
    border-radius: 50%;
    box-sizing: border-box;
  }
</style>
</head>
<body>
<div class="flyer">
  <header class="brand">
    <div class="brand-dot"></div>
    <div class="brand-name">MELBOR</div>
  </header>

  <section class="benefits">
    <h1 class="headline">Der Online-Marktplatz<br>für nachhaltige<br>Tierprodukte</h1>
    <ul class="benefit-list">
      <li><svg viewBox="0 0 52 52" fill="none" stroke="#fff" stroke-width="3.5" stroke-linecap="round" stroke-linejoin="round"><path d="M40 20 A19 19 0 1 1 30 9"/><path d="M15 26 L24 35 L46 6"/></svg>Marktplatz mit großer Produktauswahl</li>
      <li><svg viewBox="0 0 52 52" fill="none" stroke="#fff" stroke-width="3.5" stroke-linecap="round" stroke-linejoin="round"><path d="M40 20 A19 19 0 1 1 30 9"/><path d="M15 26 L24 35 L46 6"/></svg>Produkte von Manufakturen</li>
      <li><svg viewBox="0 0 52 52" fill="none" stroke="#fff" stroke-width="3.5" stroke-linecap="round" stroke-linejoin="round"><path d="M40 20 A19 19 0 1 1 30 9"/><path d="M15 26 L24 35 L46 6"/></svg>Hilfreiche Blogartikel</li>
      <li><svg viewBox="0 0 52 52" fill="none" stroke="#fff" stroke-width="3.5" stroke-linecap="round" stroke-linejoin="round"><path d="M40 20 A19 19 0 1 1 30 9"/><path d="M15 26 L24 35 L46 6"/></svg>Nachhaltiges Futtermittel</li>
      <li><svg viewBox="0 0 52 52" fill="none" stroke="#fff" stroke-width="3.5" stroke-linecap="round" stroke-linejoin="round"><path d="M40 20 A19 19 0 1 1 30 9"/><path d="M15 26 L24 35 L46 6"/></svg>Handgefertigte Accesoires</li>
      <li><svg viewBox="0 0 52 52" fill="none" stroke="#fff" stroke-width="3.5" stroke-linecap="round" stroke-linejoin="round"><path d="M40 20 A19 19 0 1 1 30 9"/><path d="M15 26 L24 35 L46 6"/></svg>Originelles Spielzeug u.v.m.</li>
    </ul>
  </section>

  <div class="photo" role="img" aria-label="Foto: Ein braun-weißer Spaniel nimmt einen Kausnack aus einer Hand, unscharfer Garten im Hintergrund"></div>

  <footer>
    <div class="website">www.melbor.de</div>
    <div class="animal-marks" role="img" aria-label="Symbole für Hund, Katze und Pferd">
      <span></span><span></span><span></span>
    </div>
  </footer>
</div>
</body>
</html>
```